Company or website name
- Comedy Juggler Website
- I am a Comedy/Technical Juggler, working for cruise lines, corporate events, and festivals around the world

```html
<!DOCTYPE html>
<html lang="en">
<head>
<meta charset="utf-8">
<title>Milo Spinwell – Comedy Juggler</title>
<link href="https://fonts.googleapis.com/css2?family=Arimo:wght@400;700&family=Lilita+One&family=Questrial&display=swap" rel="stylesheet">
<style>
:root{
  --sky-deep:#1769b3;
  --sky:#2d8fd6;
  --sky-light:#6cc4f0;
  --navy:#1d3a63;
  --nav-dark:#233c5c;
  --title-blue:#0d3c8a;
  --gold:#f6c21a;
  --white:#ffffff;
  --panel-line:#cfcfcf;
  --text:#333333;
  --label:#444444;
  --input-line:#bdbdbd;
}
*{margin:0;padding:0;box-sizing:border-box}
html,body{width:1200px;height:1085px;overflow:hidden}
body{position:relative;font-family:"Arimo",Arial,sans-serif;color:var(--text);
  background:linear-gradient(180deg,var(--sky-deep) 0%,var(--sky) 30%,var(--sky-light) 85%,#8fd3f4 100%)}
.abs{position:absolute}

/* header */
.header-photo{position:absolute;background:radial-gradient(ellipse at 50% 40%,#d9c3a8 0%,#8a8f9c 45%,rgba(45,143,214,0) 75%)}
.hero-juggler{left:430px;top:0;width:420px;height:268px}
.hero-corner-top{left:1060px;top:30px;width:140px;height:110px}
.hero-corner-bottom{left:1030px;top:150px;width:170px;height:118px}
.brand{left:60px;top:44px}
.brand-name{font-family:"Lilita One",sans-serif;font-size:50px;line-height:1;color:var(--white);letter-spacing:1px}
.brand-tagline{margin-top:14px;font-weight:700;font-size:15px;color:var(--gold)}

.top-links{left:754px;top:0;width:386px;height:50px;background:linear-gradient(#fbfbfb,#dcdcdc);
  border-radius:0 0 6px 6px;display:flex;align-items:center;font-family:"Questrial",sans-serif;font-size:17px;color:var(--navy);letter-spacing:1px}
.top-link{display:flex;align-items:center;gap:12px;padding:0 20px}
.top-link + .top-link{border-left:1px solid #b5b5b5}
.top-link svg{width:34px;height:30px}

/* navigation */
.main-nav{left:65px;top:266px;width:1075px;height:37px;background:linear-gradient(#3a5678,var(--nav-dark));
  border-radius:6px 6px 0 0;display:flex;align-items:stretch;font-family:"Questrial",sans-serif;font-size:17px;color:var(--white);letter-spacing:1px;padding-left:12px}
.nav-item{display:flex;align-items:center;padding:0 18px;border-right:1px solid #4f6a8c}
.nav-item.is-active{background:var(--gold);margin-right:13px}

/* content panel */
.content{left:65px;top:303px;width:1075px;height:695px;background:var(--white);border-radius:0 0 6px 6px}
.page-title{left:82px;top:322px;font-size:33px;font-weight:700;color:var(--title-blue)}
.intro{left:82px;top:365px;width:650px;height:124px;border:2px solid var(--panel-line);padding:12px 12px;font-size:13.5px;line-height:21px;color:var(--text)}

.video{left:82px;top:511px;width:535px;height:338px;background:var(--white);border:1px solid #d6d6d6;box-shadow:0 0 8px rgba(0,0,0,.3);padding:11px}
.video-screen{position:relative;width:100%;height:285px;background:radial-gradient(ellipse at 45% 60%,#8e8e8e 0%,#2a2a2a 45%,#000 80%)}
.video-play{position:absolute;left:206px;top:108px;width:100px;height:66px;border-radius:12px;background:rgba(40,40,40,.85);border:1px solid #777}
.video-play svg{position:absolute;left:37px;top:18px}
.video-brand{position:absolute;right:8px;bottom:8px;font-size:15px;font-weight:700;color:#cfcfcf}
.video-bar{height:28px;background:linear-gradient(#e9eef4,#b8c4d1);display:flex;align-items:center;gap:10px;padding:0 8px;font-size:12px;color:#333}
.video-track{flex:1;height:8px;border-radius:4px;background:#fff;border:1px solid #8a96a3}

.clients{left:82px;top:930px;height:44px;display:flex;align-items:center;gap:22px}
.clients-label{font-weight:700;font-size:16px;color:#222;padding-right:18px;border-right:1px solid #cfcfcf;height:44px;display:flex;align-items:center}
.client{font-weight:700;font-size:16px;color:#222;display:flex;align-items:center;gap:6px}
.client-dot{width:12px;height:12px;border-radius:50%;background:#222}

/* forms */
.card{position:absolute;background:var(--white);border:2px solid #dedede;border-radius:10px;box-shadow:0 0 6px rgba(0,0,0,.12)}
.card-head{height:50px;border-bottom:1px solid #d7d7d7;background:linear-gradient(#fff,#ececec);border-radius:10px 10px 0 0;
  display:flex;align-items:center;padding-left:18px;font-family:"Questrial",sans-serif;font-size:17px;color:#333;letter-spacing:1px}
.booking{left:775px;top:322px;width:332px;height:398px}
.members{left:775px;top:746px;width:332px;height:180px}
.field-label{position:absolute;font-size:13.5px;color:var(--label)}
.field{position:absolute;height:27px;border:1px solid var(--input-line);border-radius:4px;background:#fff;box-shadow:inset 0 1px 2px rgba(0,0,0,.12)}
.field-date-btn{position:absolute;right:3px;top:3px;width:22px;height:19px;border-radius:3px;background:#333;color:#fff;font-size:11px;text-align:center;line-height:19px}
.btn{position:absolute;height:29px;border:1px solid #aaa;border-radius:4px;background:linear-gradient(#fafafa,#dcdcdc);font-size:13.5px;color:#333;display:flex;align-items:center;justify-content:center}

/* footer */
.footer-copy{left:788px;top:1040px;font-size:15px;color:var(--white);letter-spacing:.5px}
.social-links{position:absolute;left:1018px;top:1041px;display:flex;gap:14px}
.social{display:flex;align-items:center;gap:5px;font-size:12px;color:var(--white);font-weight:700}
.social-mark{width:14px;height:14px;background:var(--white)}
</style>
</head>
<body>

<header>
  <div class="header-photo hero-juggler" role="img" aria-label="Photo of the juggler holding juggling clubs"></div>
  <div class="header-photo hero-corner-top" role="img" aria-label="Photo of the juggler upside down"></div>
  <div class="header-photo hero-corner-bottom" role="img" aria-label="Photo of the juggler catching an apple"></div>

  <div class="abs brand">
    <div class="brand-name">MILO SPINWELL</div>
    <div class="brand-tagline">Australia's Comedy Juggling Superstar</div>
  </div>

  <div class="abs top-links">
    <div class="top-link">
      <svg viewBox="0 0 34 30"><path d="M2 5h6l4 15h16l3-11H10" fill="none" stroke="#d2232a" stroke-width="3"/><circle cx="14" cy="25" r="2.5" fill="#d2232a"/><circle cx="26" cy="25" r="2.5" fill="#d2232a"/></svg>
      SHOP
    </div>
    <div class="top-link">
      <svg viewBox="0 0 34 30"><rect x="6" y="2" width="20" height="26" rx="2" fill="#8a6b3a"/><rect x="10" y="5" width="13" height="20" fill="#e6d3a3"/></svg>
      FREE LESSONS
    </div>
  </div>

  <nav class="abs main-nav">
    <div class="nav-item is-active">HOME</div>
    <div class="nav-item">BIOGRAPHY</div>
    <div class="nav-item">SHOWS</div>
    <div class="nav-item">PROMO MATERIAL</div>
    <div class="nav-item">AGENTS</div>
    <div class="nav-item">BOOKING INFO</div>
  </nav>
</header>

<main class="abs content"></main>

<h1 class="abs page-title">A Night of Quirky Mayhem</h1>
<div class="abs intro">
  Milo Spinwell is Australia's Newest Comedy Sensation.<br>
  At the tender age of 23, Milo Spinwell is one of Australia's most sought after entertainers.
  Having clients behind him such as Coral Crown Cruises, Tulip Line Cruises, Regal Lagoon Cruises, Harbour &amp; Ocean Cruises, Burger Barn, Kestrel Motors, Valemont Auto, Pantry Masters Australia to name a few.
</div>

<div class="abs video">
  <div class="video-screen" role="img" aria-label="Video still of the juggler performing on stage">
    <div class="video-play"><svg width="26" height="30" viewBox="0 0 26 30"><path d="M0 0l26 15L0 30z" fill="#fff"/></svg></div>
    <div class="video-brand">Reelbox</div>
  </div>
  <div class="video-bar">
    <svg width="14" height="14" viewBox="0 0 14 14"><path d="M2 1l11 6-11 6z" fill="#333"/></svg>
    <svg width="16" height="14" viewBox="0 0 16 14"><path d="M1 5h4l4-4v12l-4-4H1z" fill="#333"/></svg>
    <span>0:00 / 0:00</span>
    <div class="video-track"></div>
    <svg width="16" height="14" viewBox="0 0 16 14"><path d="M2 10l6-6 6 6z" fill="#333"/></svg>
    <svg width="16" height="14" viewBox="0 0 16 14"><rect x="1" y="1" width="14" height="12" fill="none" stroke="#333" stroke-width="2"/></svg>
  </div>
</div>

<div class="abs clients">
  <div class="clients-label">CLIENTS</div>
  <div class="client">Pantry</div>
  <div class="client">Fairgrounds</div>
  <div class="client">Burger</div>
  <div class="client"><span class="client-dot"></span>Kestrel</div>
  <div class="client"><span class="client-dot"></span>Valemont</div>
  <div class="client">Copyline</div>
</div>

<section class="card booking">
  <div class="card-head">BOOKING FORM</div>
</section>
<span class="field-label" style="left:795px;top:397px">Name</span>
<span class="field" style="left:900px;top:394px;width:171px"></span>
<span class="field-label" style="left:795px;top:445px">Email ID</span>
<span class="field" style="left:900px;top:442px;width:171px"></span>
<span class="field-label" style="left:795px;top:490px">Contact No</span>
<span class="field" style="left:900px;top:487px;width:171px"></span>
<span class="field-label" style="left:795px;top:533px">Event</span>
<span class="field" style="left:900px;top:530px;width:171px"></span>
<span class="field-label" style="left:795px;top:575px">Date</span>
<span class="field" style="left:900px;top:572px;width:171px"><span class="field-date-btn">v</span></span>
<span class="field-label" style="left:795px;top:614px">Message</span>
<span class="field" style="left:900px;top:614px;width:171px;height:51px"></span>
<span class="btn" style="left:891px;top:680px;width:91px">Subscribe</span>

<section class="card members">
  <div class="card-head">MEMBER'S AREA</div>
</section>
<span class="field-label" style="left:791px;top:806px">Name</span>
<span class="field" style="left:898px;top:802px;width:189px"></span>
<span class="field-label" style="left:791px;top:847px">Email Address</span>
<span class="field" style="left:898px;top:843px;width:189px"></span>
<span class="btn" style="left:890px;top:882px;width:91px">Subscribe</span>

<footer>
  <div class="abs footer-copy">© 2010 MILOSPINWELL.COM</div>
  <div class="social-links">
    <div class="social"><span class="social-mark"></span>Friendspace</div>
    <div class="social"><span class="social-mark"></span>Chirper</div>
  </div>
</footer>

</body>
</html>
```